website for shopify- Almond Steward. Natural Peanut Butter Mixer

I need a website for shopify for my invention...The AlmondSteward. ( Registered trademark)
They are kitchen accessories for mixing Natural peanut butter (9 mixing hooks). Natural peanut butter separates with oil floating to the top when it sits on the shelf. Very hard and messy to mix it in manually.

My hook is compatible with 8 popular brand name electric hand mixers, plus 1/4” HEX universal drill bit. (9 total)

The mixing Hook part that goes into the nut butter is all the same for each hook, it’s just locking interface changes for each hook. I will supply a close up photo for each hook lock mechanism. ( leave blank until Thursday next week)
Brands are: Gray and Fenwick, Vellomix, Corwin Harbor, StoveMate, Brelda, Halvern Trope, Glowline Modern, Glowline Retro.
Plus 1/4” HEX quick lock drill bit.

I would like to inspire with complementary healthy peanut butter snack images..as peanut butter is pretty brown!!
There are lots of beautiful stock photos of peanut butter snacks on framevault or Picbarn. Samples included in my files. My logo needs to have Registered trade Mark R in circle ⭕️ added to end of logo.
Plus I would like a couple of smiling moms with kids eating peanut butter.

Target Market(s)

North American health food minded people.

Coding

Number of Pages Required

5+ page

Font styles to use
Sans Serif

Colors
ffffff
ec1f27
f78f20
9bcb3c

Requirements
Must have
• I have about 6 sections in my 1 page website to design....page 7 thru 15 are all the same with just photo and brand name changes and list of model numbers compatible, for each different mixing hook.

I want my headline to rotate with 3 changing words.
Natural Peanut Butter
1) Mixed Perfectly 2) Better Tasting 3) Hassle-Free

Want to add shop now button on all pages.

Clean white background. I like shadow colour boxes behind clusters of 2-3 photos. Contemporary look.
I can type and upload blog pages soon so you don’t have to type them in. Just add a few photos.
Patented Design!!! Important to add so copy cats don’t copy.
Nice to have
• Complementary 3 colour palette that doesn’t change. Red being one.
Open to seeing other colour palettes.
Should not have
• Logos of any brand names. Just written in a clear black font consistent for all.

```html
<!DOCTYPE html>
<html lang="en">
<head>
<meta charset="utf-8">
<title>Almond Steward — Natural Peanut Butter Mixer</title>
<link rel="stylesheet" href="https://fonts.googleapis.com/css2?family=Orbitron:wght@700;900&family=Poppins:wght@400;500;600;700&display=swap">
<style>
:root{
  --white:#ffffff;
  --ink:#2b2b2b;
  --ink-soft:#555555;
  --accent:#f0906a;
  --accent-deep:#e3805d;
  --brown-dark:#9a604e;
  --brown-mid:#c27a63;
  --peach-bg:#fdebe4;
  --peach-soft:#fcefed;
  --circle-gray:#f1f1f1;
  --circle-blue:#e3effb;
  --jar-amber:#d9a257;
  --jar-amber-deep:#b87a2e;
}
*{box-sizing:border-box;margin:0;padding:0}
html,body{width:1200px;height:4525px;overflow:hidden;background:var(--white)}
body{font-family:"Poppins",sans-serif;color:var(--ink)}
.page{position:relative;width:1200px;height:4525px;overflow:hidden}
.abs{position:absolute}
.heading{font-family:"Orbitron",sans-serif;font-weight:900;letter-spacing:1px;text-align:center;color:var(--ink)}
.btn{position:absolute;display:flex;align-items:center;justify-content:center;border-radius:20px;font-family:"Poppins",sans-serif;font-weight:700;letter-spacing:.5px;text-transform:uppercase}
.btn-white{background:var(--white);color:var(--ink);font-size:14px}
.btn-dark{background:var(--brown-dark);color:var(--white);font-size:14px}
.btn-accent{background:var(--accent);color:var(--white);font-size:16px}

/* hero */
.hero{position:absolute;left:0;top:0;width:1200px;height:920px;background:linear-gradient(160deg,#d8c8b4 0%,#b89a7d 45%,#8d6c52 100%)}
.hero-wave{position:absolute;left:0;top:0}
.logo{position:absolute;left:0;width:1200px;top:22px;display:flex;flex-direction:column;align-items:center;gap:6px;color:var(--white)}
.logo-mark{width:56px;height:56px;border-radius:50%;background:var(--white);opacity:.9}
.logo-name{font-family:"Poppins",sans-serif;font-weight:500;font-size:19px;letter-spacing:2px}
.nav{position:absolute;top:30px;right:112px;display:flex;gap:22px;font-size:12px;font-weight:700;color:var(--white)}
.hero-kicker{top:266px;width:1200px;font-family:"Orbitron",sans-serif;font-weight:700;font-size:22px;color:var(--white);text-align:center;letter-spacing:1px}
.hero-title{top:288px;width:1200px;font-size:56px;color:var(--white)}
.jar-photo{position:absolute;left:488px;top:470px;width:222px;height:410px;border-radius:60px 60px 90px 90px;background:linear-gradient(180deg,#e0aa55,#c98a35);box-shadow:0 30px 40px rgba(0,0,0,.12)}
.hook-photo{position:absolute;left:88px;top:755px;width:70px;height:245px;border-radius:30px;background:linear-gradient(180deg,#8e8e8e,#c9c9c9)}
.wrap-photo{position:absolute;left:972px;top:770px;width:158px;height:158px;border-radius:50%;background:radial-gradient(circle,#f0d6b5,#d9b48a);box-shadow:0 10px 25px rgba(0,0,0,.15)}

/* how it works */
.how-title{top:950px;width:1200px;font-size:38px}
.step{position:absolute;top:1040px;width:260px;text-align:center}
.step-num{font-family:"Orbitron",sans-serif;font-weight:900;font-size:62px;color:var(--accent);line-height:1.2}
.step-text{font-size:15px;line-height:1.35;color:var(--ink-soft)}

/* offer band */
.offer-band{position:absolute;left:0;top:1240px}
.offer-bubble{position:absolute;left:498px;top:1240px;width:210px;height:210px;border-radius:50%;background:var(--brown-dark);display:flex;align-items:center;justify-content:center;color:var(--white);font-weight:700;font-size:19px}
.price{position:absolute;top:1455px;width:1200px;text-align:center;color:var(--white);font-family:"Orbitron",sans-serif;font-weight:900;font-size:78px}
.price small{font-family:"Poppins",sans-serif;font-size:22px;font-weight:700}
.offer-line{position:absolute;width:1200px;text-align:center;color:var(--white)}
.signup{position:absolute;left:341px;width:518px;height:40px;border-radius:22px;background:var(--white);display:flex;align-items:center;justify-content:space-between}
.signup-field{padding-left:26px;font-size:13px;color:var(--ink)}
.signup-btn{height:40px;width:154px;border-radius:22px;background:var(--brown-dark);color:var(--white);font-weight:700;font-size:15px;display:flex;align-items:center;justify-content:center}
.jar-left{position:absolute;left:88px;top:1472px;width:180px;height:273px;border-radius:28px;background:linear-gradient(180deg,#3a2e28 0 14%,#d3a04e 14%,#b8842f 100%);box-shadow:0 20px 30px rgba(0,0,0,.2)}
.jar-right{position:absolute;left:826px;top:1405px;width:374px;height:413px;border-radius:40px 0 0 40px;background:linear-gradient(180deg,#e8b97a,#c98f48)}

/* brands */
.brands-title{top:1990px;width:1200px;font-size:38px;line-height:1.05}
.brand{position:absolute;border-radius:50%;display:flex;align-items:center;justify-content:center;text-align:center;font-weight:600;color:var(--ink);line-height:1.1}
.brand-photo{position:absolute;border-radius:50%}

/* natural jars */
.natural-bg{position:absolute;left:0;top:2360px}
.natural-title{top:2608px;width:1200px;font-size:38px}
.natural-sub{position:absolute;top:2656px;width:1200px;text-align:center;font-family:"Orbitron",sans-serif;font-weight:700;font-size:18px;letter-spacing:1px}
.jar{position:absolute;border-radius:22px 22px 16px 16px}
.jar-caption{position:absolute;top:3004px;width:1200px;text-align:center;font-family:"Orbitron",sans-serif;font-weight:700;font-size:19px}

/* testimonials */
.reviews-title{top:3296px;width:1200px;font-size:38px}
.review{position:absolute;top:3365px;width:331px;height:179px;background:var(--white);box-shadow:0 4px 18px rgba(0,0,0,.09);padding:22px 20px}
.review::after{content:"";position:absolute;left:24px;bottom:-22px;border-left:0 solid transparent;border-right:22px solid transparent;border-top:22px solid var(--white);filter:drop-shadow(0 4px 3px rgba(0,0,0,.05))}
.review-head{display:flex;align-items:center;gap:14px}
.avatar{width:46px;height:46px;border-radius:50%;background:linear-gradient(135deg,#c7a08c,#7d5b4b)}
.review-name{font-weight:700;font-size:14px;line-height:1.1}
.review-role{font-size:11px;color:var(--ink-soft)}
.review-text{margin-top:10px;font-size:12px;line-height:1.6;color:var(--ink-soft)}
.stars{margin-top:4px;color:#f5a623;font-size:15px;letter-spacing:3px}

/* bottom signup */
.signup-band{position:absolute;left:0;top:3600px}
.signup-title{top:3862px;width:1200px;font-size:38px}
.signup-sub{position:absolute;top:3909px;width:1200px;text-align:center;font-size:18px;font-weight:500}

/* footer */
.hungry{position:absolute;top:4140px;left:330px;font-weight:600;font-size:36px}
.footer-logo{position:absolute;left:88px;top:4287px;display:flex;align-items:center;gap:14px;color:var(--brown-mid)}
.footer-logo-mark{width:60px;height:60px;border-radius:50%;background:var(--brown-mid)}
.footer-logo-name{font-weight:500;font-size:22px;letter-spacing:2px}
.footer-col{position:absolute;top:4278px;font-size:15px;line-height:28px;color:var(--ink)}
.contact{position:absolute;left:836px;top:4272px;font-size:15px}
.contact strong{font-weight:700;display:block}
.footer-input{position:absolute;left:836px;top:4354px;width:236px;height:32px;border-radius:18px;background:#ececec;font-size:11px;padding-left:20px;display:flex;align-items:center;color:var(--ink-soft)}
.footer-input svg{position:absolute;right:14px;top:9px}
.divider{position:absolute;left:88px;top:4480px;width:1022px;height:1px;background:#cfcfcf}
.copyright{position:absolute;left:88px;top:4497px;font-size:13px;font-weight:600}
.social{position:absolute;top:4502px;width:11px;height:11px;border-radius:2px;background:var(--ink)}
.to-top{position:absolute;left:1135px;top:4454px;width:28px;height:28px;border-radius:50%;background:var(--accent);display:flex;align-items:center;justify-content:center}
</style>
</head>
<body>
<main class="page">

  <!-- Hero -->
  <section class="hero" role="img" aria-label="Mother and child mixing natural peanut butter in a bright kitchen"></section>
  <svg class="hero-wave" width="1200" height="940" viewBox="0 0 1200 940" aria-hidden="true">
    <path d="M0,700 C260,640 480,770 760,715 C960,675 1090,615 1200,630 L1200,940 L0,940 Z" fill="#ffffff"/>
  </svg>
  <div class="hook-photo" role="img" aria-label="Stainless steel spiral mixing hook"></div>
  <div class="wrap-photo" role="img" aria-label="Peanut butter wrap snack on a plate"></div>
  <div class="jar-photo" role="img" aria-label="Jar of natural peanut butter with mixing hook inside"></div>

  <header>
    <div class="logo"><span class="logo-mark"></span><span class="logo-name">ALMOND STEWARD</span></div>
    <nav class="nav"><span>BLOG</span><span>HELP</span></nav>
  </header>
  <p class="abs hero-kicker">NATURAL PEANUT BUTTER</p>
  <h1 class="abs heading hero-title">MIXED PERFECTLY</h1>
  <a class="btn btn-white" style="left:530px;top:360px;width:140px;height:28px">Shop now</a>

  <!-- How it works -->
  <h2 class="abs heading how-title">HOW IT WORKS</h2>
  <div class="step" style="left:84px"><div class="step-num">01</div><p class="step-text">Use your own hand<br>mixer or drill</p></div>
  <div class="step" style="left:337px"><div class="step-num">02</div><p class="step-text">Thin-2 mm Stainless Steel hook<br>mixes without displacing oil</p></div>
  <div class="step" style="left:599px"><div class="step-num">03</div><p class="step-text">Mix it right in your<br>store-bought jar.</p></div>
  <div class="step" style="left:852px"><div class="step-num">04</div><p class="step-text">Arrow Tip breaks up settled nuts<br>creating top to bottom flow.</p></div>

  <!-- Offer band -->
  <svg class="offer-band" width="1200" height="640" viewBox="0 0 1200 640" aria-hidden="true">
    <defs>
      <linearGradient id="offerGrad" x1="0" y1="0" x2="1" y2="0">
        <stop offset="0" stop-color="#9a604e"/>
        <stop offset="1" stop-color="#eb9a7e"/>
      </linearGradient>
    </defs>
    <path d="M0,32 C200,20 420,120 640,145 C900,170 1080,110 1200,35 L1200,620 C1000,640 720,560 420,520 C240,495 100,505 0,530 Z" fill="url(#offerGrad)"/>
  </svg>
  <div class="offer-bubble">SHOP NOW</div>
  <div class="jar-left" role="img" aria-label="Sealed jar of natural peanut butter"></div>
  <div class="jar-right" role="img" aria-label="Open jar of peanut butter with hook and whole peanuts"></div>
  <p class="price">$19.99<small>USD</small></p>
  <p class="offer-line" style="top:1548px;font-family:'Orbitron',sans-serif;font-weight:700;font-size:22px;letter-spacing:1px">SIGN UP FOR FREE SHIPPING COUPON</p>
  <p class="offer-line" style="top:1580px;font-size:18px">(Valid in USA and Canada only)</p>
  <div class="signup" style="top:1616px"><span class="signup-field">Enter your email address</span><span class="signup-btn">SIGN UP</span></div>

  <!-- Brands -->
  <h2 class="abs heading brands-title">CHOOSE YOUR<br>HOOK HOW</h2>
  <div class="brand" style="left:32px;top:2040px;width:94px;height:94px;background:var(--peach-soft);font-size:14px">Glowline</div>
  <div class="brand" style="left:213px;top:2056px;width:122px;height:122px;background:var(--circle-gray);font-size:18px">Vellomix</div>
  <div class="brand-photo" style="left:95px;top:2189px;width:98px;height:98px;background:radial-gradient(circle,#6a6a6a 0 28%,#f1f1f1 30%)" role="img" aria-label="Retro hand mixer"></div>
  <div class="brand" style="left:275px;top:2197px;width:138px;height:138px;background:var(--peach-soft);font-size:15px">StoveMate</div>
  <div class="brand" style="left:416px;top:2096px;width:176px;height:176px;background:var(--circle-gray);font-size:19px">Corwin<br>Harbor</div>
  <div class="brand" style="left:613px;top:2096px;width:176px;height:176px;background:var(--peach-soft);font-size:19px">Gray and<br>Fenwick</div>
  <div class="brand" style="left:826px;top:2056px;width:122px;height:122px;background:var(--circle-blue);font-size:20px">Brelda</div>
  <div class="brand" style="left:886px;top:2184px;width:126px;height:126px;background:#e6e6e6;font-size:15px">Halvern<br>Trope</div>
  <div class="brand-photo" style="left:1047px;top:2165px;width:154px;height:154px;background:linear-gradient(120deg,#f1f1f1 40%,#c9a24a 55%,#3a3a3a 80%)" role="img" aria-label="Quarter inch hex drill bit"></div>

  <!-- Natural jars -->
  <svg class="natural-bg" width="1200" height="830" viewBox="0 0 1200 830" aria-hidden="true">
    <defs>
      <linearGradient id="peachGrad" x1="0" y1="0" x2="0" y2="1">
        <stop offset="0" stop-color="#fcded3"/>
        <stop offset=".55" stop-color="#fdeee8"/>
        <stop offset="1" stop-color="#ffffff"/>
      </linearGradient>
    </defs>
    <path d="M0,60 C220,150 520,150 800,110 C1000,80 1120,20 1200,0 L1200,820 L0,820 Z" fill="url(#peachGrad)"/>
  </svg>
  <h2 class="abs heading natural-title">MIXES IN ALL NATURAL</h2>
  <p class="natural-sub">NUT BUTTERS RIGHT IN THEIR OWN JARS.</p>
  <div class="jar" style="left:158px;top:2764px;width:97px;height:206px;background:linear-gradient(180deg,#f0c877,#e6b05c)" role="img" aria-label="Jar of cashew butter"></div>
  <div class="jar" style="left:302px;top:2768px;width:120px;height:202px;background:linear-gradient(180deg,#b7cfc0,#8aa88f)" role="img" aria-label="Jar of macadamia nut butter"></div>
  <div class="jar" style="left:466px;top:2706px;width:265px;height:281px;background:linear-gradient(180deg,#f2f2f2 0 14%,#c98a45 14%,#b0743a 100%);box-shadow:0 18px 26px rgba(0,0,0,.12)" role="img" aria-label="Jar of almond butter"></div>
  <div class="jar" style="left:768px;top:2762px;width:125px;height:208px;background:linear-gradient(180deg,#f0d9a6,#d9b676)" role="img" aria-label="Jar of tahini sesame paste"></div>
  <div class="jar" style="left:922px;top:2764px;width:136px;height:206px;background:linear-gradient(180deg,#e3e3e3 0 14%,#8a4a2e 14%,#6f3a24 100%)" role="img" aria-label="Jar of hazelnut butter"></div>
  <p class="jar-caption">ALMON BUTTER</p>
  <a class="btn btn-dark" style="left:530px;top:3043px;width:140px;height:28px">Shop now</a>

  <!-- Testimonials -->
  <h2 class="abs heading reviews-title">WHAT PEOPLE ARE SAYING...</h2>
  <article class="review" style="left:91px">
    <div class="review-head"><span class="avatar" role="img" aria-label="Customer portrait"></span><div><p class="review-name">JOHN SMITH</p><p class="review-role">Co Founder</p></div></div>
    <p class="review-text">"Lorem Ipsum is simply dummy text of the printing and typesetting industry. Lorem Ipsum has been the industry's standard dummy"</p>
    <p class="stars">★★★★★</p>
  </article>
  <article class="review" style="left:434px">
    <div class="review-head"><span class="avatar" role="img" aria-label="Customer portrait"></span><div><p class="review-name">JOHN SMITH</p><p class="review-role">Co Founder</p></div></div>
    <p class="review-text">"Lorem Ipsum is simply dummy text of the printing and typesetting industry. Lorem Ipsum has been the industry's standard dummy"</p>
    <p class="stars">★★★★★</p>
  </article>
  <article class="review" style="left:778px">
    <div class="review-head"><span class="avatar" role="img" aria-label="Customer portrait"></span><div><p class="review-name">JOHN SMITH</p><p class="review-role">Co Founder</p></div></div>
    <p class="review-text">"Lorem Ipsum is simply dummy text of the printing and typesetting industry. Lorem Ipsum has been the industry's standard dummy"</p>
    <p class="stars">★★★★★</p>
  </article>

  <!-- Bottom signup -->
  <svg class="signup-band" width="1200" height="486" viewBox="0 0 1200 486" role="img" aria-label="Peanut butter snacks in warm orange tones">
    <defs>
      <linearGradient id="signupGrad" x1="0" y1="0" x2="1" y2="1">
        <stop offset="0" stop-color="#f3a481"/>
        <stop offset="1" stop-color="#ef9a72"/>
      </linearGradient>
    </defs>
    <path d="M0,22 C220,70 460,180 700,150 C920,125 1100,60 1200,20 L1200,486 L0,486 Z" fill="url(#signupGrad)"/>
  </svg>
  <h2 class="abs heading signup-title">SIGN UP FOR FREE SHIPPING + GET</h2>
  <p class="signup-sub">12 Natural Peanut Butter Mixing Hacks!....That actually Work</p>
  <div class="signup" style="top:3946px"><span class="signup-field">Enter your email address</span><span class="signup-btn">SIGN UP</span></div>

  <!-- Footer -->
  <p class="hungry">Hungry for more?</p>
  <a class="btn btn-accent" style="left:708px;top:4153px;width:156px;height:36px">Shop now</a>

  <footer>
    <div class="footer-logo"><span class="footer-logo-mark"></span><span class="footer-logo-name">ALMOND STEWARD</span></div>
    <ul class="footer-col" style="left:446px;list-style:none"><li>Shop</li><li>Hooks</li><li>BLogs</li></ul>
    <ul class="footer-col" style="left:629px;list-style:none"><li>Help</li><li>Peanut Butter</li><li>Recipes</li><li>Return +</li><li>Warranty</li></ul>
    <div class="contact">
      <strong>Contact Us</strong>
      <span>info@almondsteward.com</span>
      <strong style="margin-top:6px">Signup for free shipplngs</strong>
    </div>
    <div class="footer-input">Email address
      <svg width="14" height="14" viewBox="0 0 14 14" aria-hidden="true"><path d="M1,7 L13,1 L9,13 L7,8 Z" fill="#f0906a"/></svg>
    </div>
    <div class="divider"></div>
    <p class="copyright">Copyright 2021 | All Rights Reserved</p>
    <span class="social" style="left:1079px" aria-label="Social link"></span>
    <span class="social" style="left:1096px" aria-label="Social link"></span>
    <span class="to-top" aria-label="Back to top">
      <svg width="12" height="8" viewBox="0 0 12 8" aria-hidden="true"><path d="M1,7 L6,2 L11,7" stroke="#ffffff" stroke-width="2" fill="none"/></svg>
    </span>
  </footer>

</main>
</body>
</html>
```